Simple Floral Service Web-Banner

I need to put a banner add on the members section of a website for an organization in which we are members.

The ad size is 470px x 214px.

I am uploading 4 pictures. 1 is a picture of red roses, and 1 is a picture of a t-shirt. These are 2 major products of ours which need to be incorporated in the banner. I do not have these in higher res or vectorized format, so please work with what you have. I am also uploading our 2 logos, one is for our Canadian company, and one for our American company. Both logos should be included at equal sizes.

The following text should be used:
"Proudly providing top quality roses, and custom commemorative grad t-shirts at over 800 schools."

I am just looking for a simple banner incorporating those pictures and that wording. I don't want something that is overly flashy.

I will monitor the submissions in a timely manner and give you feedback.

```html
<!DOCTYPE html>
<html lang="en">
<head>
<meta charset="utf-8">
<title>Floral Service Banner</title>
<link rel="stylesheet" href="https://fonts.googleapis.com/css2?family=Open+Sans:wght@400;600&display=swap">
<style>
  :root {
    --page-grey: #e8e8e8;
    --plum: #8a1e5c;
    --leaf: #8cba5f;
    --lime: #b5d95a;
    --white: #ffffff;
    --shirt-light: #e4e4e4;
    --shirt-mid: #c9c9c9;
    --rose-red: #b3121c;
    --rose-bg: #6b3a22;
  }
  * { margin: 0; padding: 0; box-sizing: border-box; }
  html, body {
    width: 1200px;
    height: 661px;
    overflow: hidden;
    background: var(--page-grey);
    font-family: "Open Sans", Arial, sans-serif;
  }
  .banner {
    position: absolute;
    left: 125px;
    top: 107px;
    width: 944px;
    height: 432px;
    background: var(--leaf);
  }
  .banner__band {
    position: absolute;
    left: 0;
    top: 0;
    width: 100%;
    height: 81px;
    background: var(--plum);
  }
  .banner__frame {
    position: absolute;
    left: 174px;
    top: 0;
    width: 594px;
    height: 311px;
    background: var(--plum);
  }
  .brand {
    position: absolute;
    top: 16px;
    display: flex;
    align-items: center;
    gap: 8px;
    color: var(--lime);
    font-weight: 600;
    font-size: 22px;
    line-height: 1.1;
  }
  .brand__mark {
    width: 12px;
    height: 12px;
    background: var(--lime);
    flex: none;
  }
  .brand--canada { left: 14px; }
  .brand--usa { right: 14px; text-align: right; }
  .product {
    position: absolute;
    top: 67px;
    height: 238px;
  }
  .product--shirt {
    left: 184px;
    width: 282px;
    background: linear-gradient(135deg, var(--shirt-light), var(--shirt-mid));
  }
  .product--roses {
    left: 476px;
    width: 288px;
    background: radial-gradient(ellipse at 45% 45%, var(--rose-red) 0%, #8e1a1c 45%, var(--rose-bg) 100%);
  }
  .banner__tagline {
    position: absolute;
    left: 0;
    top: 330px;
    width: 100%;
    text-align: center;
    color: var(--white);
    font-size: 28px;
    line-height: 40px;
  }
</style>
</head>
<body>
  <section class="banner">
    <div class="banner__band"></div>
    <div class="banner__frame"></div>

    <div class="brand brand--canada">
      <span class="brand__mark"></span>
      <span>Laurel Lane<br>Flowers</span>
    </div>
    <div class="brand brand--usa">
      <span>Tassel Row<br>Flowers</span>
      <span class="brand__mark"></span>
    </div>

    <div class="product product--shirt" role="img" aria-label="White commemorative graduation t-shirts, front with school crest and back listing the graduating class"></div>
    <div class="product product--roses" role="img" aria-label="Bouquet of a dozen red roses with baby's breath wrapped with a red ribbon"></div>

    <p class="banner__tagline">"Proudly providing top quality roses,<br>and custom commemorative grad t-shirts at over 800 schools."</p>
  </section>
</body>
</html>
```